Modern business card design for professional copywriter

I'd like a business card design that I can use to have my cards printed out by plink.com as a squared corners business card (see artwork and design guidelines here: https://help.plink.com/hc/en-gb/sections/300481726-PLINK-Product-Templates)

The design should be clean and modern and reflect the colours, tone and branding on my website: https://noravestrel.com.au

Target Market(s)

Professionals, B2B small business owners

Industry/Entity Type

Business

Contact Information for Business Card

Nora Vestrel
m: 0427 593 864
e: nora@noravestrel.com.au
w: noravestrel.com.au

Font styles to use
Sans Serif

Requirements
Must have
• Tagline: "Smart copywriting for clever business people"
• Brand colours: fd8000, 009984, 666666 and black
Nice to have

```html
<!DOCTYPE html>
<html lang="en">
<head>
<meta charset="utf-8">
<title>Nora Vestrel — Business Card</title>
<link rel="stylesheet" href="https://fonts.googleapis.com/css2?family=Open+Sans:wght@400;600;700&display=swap">
<style>
  :root {
    --teal: #149e89;
    --orange: #fd8000;
    --grey: #666666;
    --ink: #222222;
    --white: #ffffff;
    --backdrop: #eeeeec;
  }
  * { box-sizing: border-box; margin: 0; padding: 0; }
  html, body {
    width: 1200px;
    height: 900px;
    overflow: hidden;
    background: var(--backdrop);
    font-family: "Open Sans", Arial, sans-serif;
  }
  .stage { position: relative; width: 1200px; height: 900px; }
  .card {
    position: absolute;
    left: 340px;
    width: 520px;
    height: 318px;
    overflow: hidden;
    box-shadow: 0 8px 20px rgba(0,0,0,0.16);
  }
  .card--front {
    top: 112px;
    background: var(--teal);
    color: var(--white);
  }
  .card--back {
    top: 470px;
    background: var(--white);
  }
  .brand-name {
    position: absolute;
    font-weight: 700;
    font-size: 44px;
    letter-spacing: -0.5px;
    line-height: 1;
    display: flex;
    align-items: center;
    gap: 12px;
    white-space: nowrap;
  }
  .brand-name__mark {
    width: 14px;
    height: 14px;
    border-radius: 50%;
    background: currentColor;
    flex: none;
  }
  .card--front .brand-name {
    left: 0;
    right: 0;
    top: 96px;
    justify-content: center;
    color: var(--white);
  }
  .card--back .brand-name { left: 52px; top: 62px; color: var(--teal); }
  .tagline {
    position: absolute;
    left: 0;
    right: 0;
    bottom: 62px;
    text-align: center;
    font-weight: 700;
    font-size: 14px;
    letter-spacing: 0.2px;
    text-transform: uppercase;
    white-space: nowrap;
  }
  .person {
    position: absolute;
    left: 52px;
    top: 180px;
    font-size: 20px;
    font-weight: 600;
    letter-spacing: 1px;
    line-height: 1;
    text-transform: uppercase;
  }
  .person__first { color: var(--teal); }
  .person__last { color: var(--orange); }
  .contact {
    position: absolute;
    left: 52px;
    top: 214px;
    list-style: none;
    font-size: 15px;
    color: var(--ink);
  }
  .contact li {
    display: flex;
    align-items: center;
    gap: 12px;
    height: 24px;
    white-space: nowrap;
  }
  .contact svg { width: 14px; height: 14px; fill: var(--teal); flex: none; }
</style>
</head>
<body>
<main class="stage">
  <section class="card card--front" aria-label="Card front">
    <div class="brand-name"><span class="brand-name__mark"></span>Nora Vestrel</div>
    <p class="tagline">Smart copywriting for clever business people</p>
  </section>

  <section class="card card--back" aria-label="Card back">
    <div class="brand-name"><span class="brand-name__mark"></span>Nora Vestrel</div>
    <p class="person"><span class="person__first">Nora</span> <span class="person__last">Vestrel</span></p>
    <ul class="contact">
      <li>
        <svg viewBox="0 0 14 14" aria-hidden="true"><path d="M4 0h6a1 1 0 0 1 1 1v12a1 1 0 0 1-1 1H4a1 1 0 0 1-1-1V1a1 1 0 0 1 1-1zm0.5 1.5v9h5v-9zM7 11.5a0.8 0.8 0 1 0 0 1.6a0.8 0.8 0 1 0 0-1.6z"/></svg>
        <span>0427 593 864</span>
      </li>
      <li>
        <svg viewBox="0 0 14 14" aria-hidden="true"><path d="M0 3h14v8H0zM1 4l6 4.5L13 4z" fill-rule="evenodd"/></svg>
        <span>nora@noravestrel.com.au</span>
      </li>
      <li>
        <svg viewBox="0 0 14 14" aria-hidden="true"><circle cx="7" cy="7" r="7"/><path d="M3 6l3 1 1 3 1-2 2-1-3-2z" fill="#ffffff"/></svg>
        <span>noravestrel.com.au</span>
      </li>
    </ul>
  </section>
</main>
</body>
</html>
```